WEBSITE NEEDED FOR MY COMPANY CALLED BRAVERIDGE HOCKEY DEVELOPMENT

LOOKING FOR A WEBSITE TO MARKET AND SEEL MY HOCKEY DEVELOPMENT PROGRAMS.
NEEDS TO HAVE 5+ PAGES

Target Market(s)

YOUTH SPORTS

Industry/Entity Type

YOUTH ATHLETE DEVELOPMENT

Number of Pages Required

5+ page

Font styles to use
Sans Serif

Colors
0054AA
0677BA
7BADD7
CADEEF
E8F1F8

Requirements
Must have
• MAIN PAGE - SPIRNG PROGRAM PAGE - SUMMER PROGRAM PAGE - WINTER PAGE - TOURNAMENT PAGE
Nice to have
• FLASH
Should not have
• NOT SURE

```html
<!DOCTYPE html>
<html lang="en">
<head>
<meta charset="utf-8">
<title>Braveridge Hockey Development</title>
<link href="https://fonts.googleapis.com/css2?family=Bebas+Neue&family=Montserrat:wght@400;500;600&family=Oswald:wght@300;400;500;600&display=swap" rel="stylesheet">
<style>
:root{
  --sky:#33bdee;
  --sky-soft:#5ccbf1;
  --navy:#1f2d3d;
  --ink:#22303f;
  --steel:#2c5f7e;
  --band:#2e3d4e;
  --white:#ffffff;
  --muted:#7b8794;
  --ice:#eef2f5;
}
*{margin:0;padding:0;box-sizing:border-box}
html,body{width:1200px;height:2671px;overflow:hidden}
body{position:relative;font-family:'Montserrat',sans-serif;color:var(--ink);background:var(--white)}
.abs{position:absolute}
.display{font-family:'Bebas Neue','Oswald',sans-serif;font-weight:400;line-height:.92;letter-spacing:.5px}
.btn{position:absolute;display:flex;align-items:center;justify-content:center;gap:8px;border-radius:16px;font-size:12px;font-weight:600;white-space:nowrap}
.btn svg{width:10px;height:10px}

/* header */
.logo-block{left:0;top:0;width:283px;height:104px}
.brand{position:absolute;left:70px;top:28px;width:190px;display:flex;align-items:center;gap:10px;color:var(--white);font-size:12px;font-weight:600;line-height:1.35;letter-spacing:1px}
.brand i{flex:none;width:44px;height:44px;border-radius:50%;background:var(--sky)}
.navbar{left:280px;top:21px;width:920px;height:62px;background:var(--sky)}
.nav{position:absolute;left:17px;top:0;width:580px;height:62px;display:flex;align-items:center;justify-content:space-between;font-size:9.6px;color:var(--white);white-space:nowrap}
.nav .active{font-weight:600;position:relative}
.nav .active::after{content:"";position:absolute;left:8px;top:20px;width:14px;height:2px;background:var(--white)}
.signup{left:620px;top:15px;width:75px;height:31px;background:var(--white);color:var(--sky)}
.login{left:704px;top:15px;width:76px;height:31px;border:2px solid var(--white);color:var(--white)}

/* hero */
.hero{left:0;top:0;width:1200px;height:614px;background:linear-gradient(120deg,#f4f6f8 0%,#e7ecf0 60%,#dde4ea 100%);z-index:-1}
.hero-photo{left:640px;top:110px;width:560px;height:504px;background:radial-gradient(ellipse at 55% 50%,#cfd8e2 0%,#b7c4d3 45%,rgba(221,228,234,0) 75%)}
.hero-disc{left:-202px;top:202px;width:276px;height:276px;border-radius:50%;background:var(--sky)}
.eyebrow{left:172px;top:196px;font-size:15px;letter-spacing:4px;color:var(--sky);font-weight:500}
.hero-title{left:170px;top:232px;font-size:82px;color:var(--ink)}
.hero-text{left:172px;top:397px;width:440px;font-size:11.5px;line-height:22px;color:var(--ink)}
.read-more{left:172px;top:486px;width:104px;height:30px;background:var(--sky);color:var(--white)}
.contact-btn{left:290px;top:486px;width:107px;height:30px;border:1.5px solid var(--sky);color:var(--sky)}

/* about */
.about{left:0;top:614px;width:1200px;height:413px;overflow:hidden;background:var(--sky)}
.about-photo{left:0;top:0;width:620px;height:413px;background:radial-gradient(ellipse at 60% 45%,rgba(31,80,110,.28) 0%,rgba(51,189,238,0) 65%)}
.dash{width:34px;height:4px;background:var(--white)}
.about h2{position:absolute;left:172px;top:122px;font-size:64px;color:var(--navy)}
.about p{position:absolute;left:172px;top:198px;width:390px;font-size:14.5px;line-height:22px;color:var(--white)}
.about .lorem{left:172px;top:289px;width:128px;height:32px;border:2px solid var(--white);color:var(--white)}
.trainer-head{position:absolute;left:832px;top:104px;display:flex;align-items:center;gap:9px;color:var(--white)}
.arrow-dot{width:24px;height:24px;border-radius:50%;display:flex;align-items:center;justify-content:center}
.arrow-dot svg{width:12px;height:12px}
.trainer-head span{font-family:'Oswald',sans-serif;font-weight:300;font-size:30px;letter-spacing:3px;margin-left:6px}
.trainer-photo{left:820px;top:166px;width:200px;height:177px;border:3px solid var(--white);border-radius:10px;background:linear-gradient(160deg,#8a6f5f,#5a4a43 55%,#2a2b2f);box-shadow:0 6px 18px rgba(0,0,0,.25)}
.trainer-name{right:393px;top:286px;text-align:right;font-size:34px;color:var(--white)}

/* news */
.section-dash{left:583px;top:1089px;width:34px;height:4px;background:var(--sky)}
.news-title{left:0;top:1118px;width:1200px;text-align:center;font-size:68px}
.news-title b{color:var(--sky);font-weight:400}
.news-title span{color:var(--ink)}
.news-intro{left:230px;top:1198px;width:740px;text-align:center;font-size:14px;line-height:22px;color:var(--ink)}
.card{position:absolute;top:1278px;width:418px;height:242px;overflow:hidden}
.card .photo{position:absolute;inset:0}
.card svg.panel{position:absolute;inset:0}
.card .body{position:absolute;right:27px;top:26px;width:200px;text-align:right;color:var(--white)}
.card time{font-size:10px}
.card h3{font-family:'Oswald',sans-serif;font-weight:500;font-size:13px;line-height:19px;margin-top:6px}
.card p{font-size:10.5px;line-height:22px;margin-top:2px}
.card .more{right:27px;top:195px;width:104px;height:24px;border:1.5px solid var(--white);color:var(--white);font-size:9.5px;font-weight:500}
.all-news{left:536px;top:1551px;width:128px;height:32px;border:2px solid var(--ink);color:var(--ink);font-size:12px}

/* stats */
.stats{left:0;top:1668px;width:1200px;height:306px;background:var(--band);overflow:hidden}
.stats-shade{left:0;top:0;width:1200px;height:306px;background:radial-gradient(ellipse at 15% 70%,rgba(0,0,0,.25),transparent 55%),radial-gradient(ellipse at 85% 30%,rgba(0,0,0,.22),transparent 50%)}
.stat{position:absolute;top:30px;width:200px;text-align:center;color:var(--white)}
.stat svg{width:64px;height:66px}
.stat .num{font-family:'Oswald',sans-serif;font-weight:500;font-size:34px;margin-top:14px;line-height:1}
.stat .num sup{font-size:14px;vertical-align:18px;margin-left:8px}
.stat .label{font-size:10.5px;margin-top:6px;letter-spacing:.2px}

/* promo cards */
.promo{position:absolute;top:1894px;width:375px;height:271px;border-radius:22px;background:linear-gradient(135deg,#fafbfc,#eef1f4);box-shadow:0 8px 24px rgba(0,0,0,.06)}
.promo h3{position:absolute;left:34px;top:48px;font-size:38px;color:var(--ink)}
.promo p{position:absolute;left:34px;top:99px;width:300px;font-size:10.5px;line-height:22px;color:var(--muted)}
.promo .shop{left:34px;top:189px;width:128px;height:32px;border:1.5px solid var(--sky);color:var(--sky);font-weight:500}
.player{position:absolute;background:radial-gradient(ellipse at 50% 50%,#c9ced9 0%,#9aa7c2 45%,rgba(255,255,255,0) 72%);z-index:2}

/* footer */
.footer{left:0;top:2235px;width:1200px;height:436px;background:var(--sky)}
.foot-brand{position:absolute;left:175px;top:106px;display:flex;align-items:center;gap:12px;color:var(--navy);font-size:13px;font-weight:600;letter-spacing:1px;line-height:1.4}
.foot-brand i{flex:none;width:88px;height:88px;border-radius:50%;background:var(--navy)}
.foot-about{left:172px;top:224px;width:240px;font-size:10.5px;line-height:22px;color:var(--white)}
.socials{position:absolute;left:172px;top:290px;display:flex;gap:11px}
.socials i{width:23px;height:23px;border:1.5px solid var(--white);border-radius:50%}
.foot-col h4{font-family:'Oswald',sans-serif;font-weight:500;font-size:23px;color:var(--white);margin-bottom:12px}
.links{left:553px;top:164px}
.links li{list-style:none;display:flex;align-items:center;gap:9px;height:28px;font-size:10.5px;font-weight:600;color:var(--white)}
.links li svg{width:15px;height:15px}
.contact{left:874px;top:164px}
.contact li{list-style:none;display:flex;align-items:center;gap:8px;height:26px;font-size:10.5px;color:var(--white)}
.contact li svg{width:11px;height:11px}
.subscribe{left:872px;top:2545px;width:156px;height:25px;background:var(--white);border-radius:13px;z-index:3}
.subscribe span{position:absolute;left:12px;top:7px;font-size:7px;color:#aab3bb}
.subscribe b{position:absolute;right:0;top:0;width:25px;height:25px;border-radius:50%;background:var(--navy);color:var(--white);font-size:9px;font-weight:500;display:flex;align-items:center;justify-content:center}
.foot-rule{left:172px;top:2633px;width:856px;height:1px;background:rgba(255,255,255,.6)}
.copyright{left:0;top:2645px;width:1200px;text-align:center;font-size:9.5px;color:var(--white)}
</style>
</head>
<body>

<!-- hero -->
<div class="abs hero"></div>
<div class="abs hero-photo" role="img" aria-label="Photo of a hockey player in a white jersey skating with a stick"></div>
<div class="abs hero-disc"></div>
<div class="abs eyebrow">DEVELOPMENT</div>
<h1 class="abs display hero-title">BRAVERIDGE HOCKEY<br>DEVELOPMENT</h1>
<p class="abs hero-text">Amet minim mollit non deserunt ullamco est sit aliqua dolor do amet sint. Velit officia consequat duis enim velit mollit. Exercitation veniam consequat sunt nostrud amet.</p>
<a class="btn read-more">Read More <svg viewBox="0 0 12 12"><path d="M1 6h9M6 2l4 4-4 4" stroke="currentColor" stroke-width="1.6" fill="none"/></svg></a>
<a class="btn contact-btn">Contact Us <svg viewBox="0 0 12 12"><path d="M1 6h9M6 2l4 4-4 4" stroke="currentColor" stroke-width="1.6" fill="none"/></svg></a>

<!-- header -->
<svg class="abs logo-block" viewBox="0 0 283 104"><polygon points="0,0 283,0 238,104 0,104" fill="#1f2d3d"/></svg>
<div class="brand"><i></i>BRAVERIDGE HOCKEY DEVELOPMENT</div>
<div class="abs navbar">
  <nav class="nav">
    <span class="active">HOME</span>
    <span>SPIRNG PROGRAM PAGE</span>
    <span>SUMMER PROGRAM PAGE</span>
    <span>WINTER PAGE</span>
    <span>TOURNAMENT PAGE</span>
  </nav>
  <a class="btn signup">Sign Up</a>
  <a class="btn login">Log In</a>
</div>

<!-- about -->
<section class="abs about">
  <div class="abs about-photo" role="img" aria-label="Blue-tinted photo of a player handling the puck"></div>
  <svg class="abs" style="left:0;top:0" width="1200" height="413" viewBox="0 0 1200 413">
    <polygon points="830,0 1200,0 1200,413 485,413" fill="#2c5f7e"/>
    <circle cx="1265" cy="226" r="138" fill="#ffffff"/>
  </svg>
  <div class="abs dash" style="left:180px;top:92px"></div>
  <h2 class="display">ABOUT US</h2>
  <p>Amet minim mollit non deserunt ullamco est sit aliqua dolor do amet sint. Velit officia consequat duis enim velit mollit.</p>
  <a class="btn lorem">Lorem Ipsum</a>
  <div class="trainer-head">
    <div class="arrow-dot" style="background:var(--navy)"><svg viewBox="0 0 12 12"><path d="M11 6H2M6 2L2 6l4 4" stroke="#fff" stroke-width="1.6" fill="none"/></svg></div>
    <div class="arrow-dot" style="background:var(--white)"><svg viewBox="0 0 12 12"><path d="M1 6h9M6 2l4 4-4 4" stroke="#1f2d3d" stroke-width="1.6" fill="none"/></svg></div>
    <span>TRAINERS</span>
  </div>
  <div class="abs trainer-photo" role="img" aria-label="Portrait photo of the trainer"></div>
  <div class="abs display trainer-name">DORIAN<br>HALE</div>
</section>

<!-- news -->
<div class="abs section-dash"></div>
<h2 class="abs display news-title"><b>OUR</b> <span>NEW</span></h2>
<p class="abs news-intro">Amet minim mollit non deserunt ullamco est sit aliqua dolor do amet sint. Velit officia consequat duis enim velit mollit. Exercitation veniam consequat sunt nostrud amet.</p>

<article class="card" style="left:172px">
  <div class="photo" role="img" aria-label="Photo of a stick and puck on an indoor rink" style="background:linear-gradient(135deg,#a07a4e,#d9d2c8 45%,#e9edf0)"></div>
  <svg class="panel" viewBox="0 0 418 242"><polygon points="230,0 418,0 418,242 235,242 182,110" fill="#33bdee"/></svg>
  <div class="body"><time>Nov 20, 2015</time><h3>NULLAM ENIM ANTE, VOLUTPAT<br>NON VIVERRA EGET</h3><p>Vivamus hendrerit, tortor sed luctus maximus, nunc urna hendrerit nibh, sit amet efficitur libero.</p></div>
  <a class="btn more">Read More <svg viewBox="0 0 12 12"><path d="M1 6h9M6 2l4 4-4 4" stroke="currentColor" stroke-width="1.6" fill="none"/></svg></a>
</article>
<article class="card" style="left:609px">
  <div class="photo" role="img" aria-label="Photo of two youth players chasing the puck" style="background:linear-gradient(135deg,#c94a4a,#e8e2e0 50%,#dfe6ec)"></div>
  <svg class="panel" viewBox="0 0 418 242"><polygon points="230,0 418,0 418,242 235,242 182,110" fill="#33bdee"/></svg>
  <div class="body"><time>Nov 20, 2015</time><h3>NULLAM ENIM ANTE, VOLUTPAT<br>NON VIVERRA EGET</h3><p>Vivamus hendrerit, tortor sed luctus maximus, nunc urna hendrerit nibh, sit amet efficitur libero.</p></div>
  <a class="btn more">Read More <svg viewBox="0 0 12 12"><path d="M1 6h9M6 2l4 4-4 4" stroke="currentColor" stroke-width="1.6" fill="none"/></svg></a>
</article>
<a class="btn all-news">All News</a>

<!-- stats -->
<section class="abs stats">
  <div class="abs stats-shade" role="img" aria-label="Dark photo of skates on ice"></div>
  <div class="stat" style="left:103px">
    <svg viewBox="0 0 64 66" fill="none" stroke="#fff" stroke-width="3"><circle cx="28" cy="18" r="13"/><path d="M6 60c0-14 10-23 22-23 4 0 8 1 11 3"/><path d="M50 42v18M41 51h18"/></svg>
    <div class="num">120<sup>+</sup></div><div class="label">ACTIVE MEMBER</div>
  </div>
  <div class="stat" style="left:359px">
    <svg viewBox="0 0 64 66" fill="none" stroke="#fff" stroke-width="3"><rect x="5" y="10" width="54" height="52" rx="3"/><path d="M5 22h54M17 4v12M47 4v12M25 4v12M39 4v12"/><circle cx="32" cy="42" r="11"/><path d="M27 42l4 4 7-7"/></svg>
    <div class="num">20<sup>+</sup></div><div class="label">YEARLY EVENT</div>
  </div>
  <div class="stat" style="left:617px">
    <svg viewBox="0 0 64 66" fill="none" stroke="#fff" stroke-width="3"><path d="M14 2l22 50c2 5-2 10-8 10H12c-4 0-6-4-4-7"/><path d="M50 2L28 52c-2 5 2 10 8 10h16c4 0 6-4 4-7"/><circle cx="32" cy="24" r="5"/></svg>
    <div class="num">25<sup>+</sup></div><div class="label">AVAILABLE FIELD</div>
  </div>
  <div class="stat" style="left:888px">
    <svg viewBox="0 0 64 66" fill="none" stroke="#fff" stroke-width="3"><path d="M8 16h48L32 42z"/><path d="M32 42v20M20 62h24M40 16L52 2"/><circle cx="30" cy="24" r="3"/></svg>
    <div class="num">18<sup>+</sup></div><div class="label">RESTAURANT &amp; BAR</div>
  </div>
</section>

<!-- footer -->
<footer class="abs footer">
  <div class="foot-brand"><i></i>BRAVERIDGE HOCKEY<br>DEVELOPMENT</div>
  <p class="abs foot-about">Amet minim mollit non deserunt ullamco est sit aliqua dolor do amet sint.</p>
  <div class="socials"><i></i><i></i><i></i><i></i><i></i></div>
  <div class="abs foot-col links">
    <h4>Useful Links</h4>
    <ul>
      <li><svg viewBox="0 0 16 16" fill="none" stroke="#fff" stroke-width="1.3"><circle cx="8" cy="8" r="7"/><path d="M4.5 8h6M8 5.5L10.5 8 8 10.5"/></svg>HOME</li>
      <li><svg viewBox="0 0 16 16" fill="none" stroke="#fff" stroke-width="1.3"><circle cx="8" cy="8" r="7"/><path d="M4.5 8h6M8 5.5L10.5 8 8 10.5"/></svg>SPIRNG PROGRAM PAGE</li>
      <li><svg viewBox="0 0 16 16" fill="none" stroke="#fff" stroke-width="1.3"><circle cx="8" cy="8" r="7"/><path d="M4.5 8h6M8 5.5L10.5 8 8 10.5"/></svg>SUMMER PROGRAM PAGE</li>
      <li><svg viewBox="0 0 16 16" fill="none" stroke="#fff" stroke-width="1.3"><circle cx="8" cy="8" r="7"/><path d="M4.5 8h6M8 5.5L10.5 8 8 10.5"/></svg>WINTER PAGE</li>
      <li><svg viewBox="0 0 16 16" fill="none" stroke="#fff" stroke-width="1.3"><circle cx="8" cy="8" r="7"/><path d="M4.5 8h6M8 5.5L10.5 8 8 10.5"/></svg>TOURNAMENT PAGE</li>
    </ul>
  </div>
  <div class="abs foot-col contact">
    <h4>Contact Us</h4>
    <ul>
      <li><svg viewBox="0 0 12 12" fill="#fff"><path d="M6 0a4 4 0 0 0-4 4c0 3 4 8 4 8s4-5 4-8a4 4 0 0 0-4-4zm0 5.5A1.5 1.5 0 1 1 6 2.5a1.5 1.5 0 0 1 0 3z"/></svg>48 Frost Lane, Ridgeport</li>
      <li><svg viewBox="0 0 12 12" fill="none" stroke="#fff" stroke-width="1.2"><rect x="0.6" y="2" width="10.8" height="8"/><path d="M0.6 2L6 6.5 11.4 2"/></svg>hello@braveridgehockey.com</li>
      <li><svg viewBox="0 0 12 12" fill="#fff"><path d="M2.5 0.5l2 2.5-1.2 1.5c.8 1.7 2 2.9 3.7 3.7L8.5 7l2.5 2-1 2.5C5 11.5.5 7 .5 2z"/></svg>555-014-2290</li>
    </ul>
  </div>
</footer>
<div class="abs subscribe"><span>Enter Your Email</span><b>GO</b></div>
<div class="abs foot-rule"></div>
<div class="abs copyright">Copyright 2022 Mara Linden. All Rights Reserved</div>

<!-- promo cards and players -->
<div class="promo" style="left:208px">
  <h3 class="display">GET YOUR GOODS</h3>
  <p>Amet minim mollit non deserunt ullamco est sit aliqua dolor do amet sint. Velit officia consequat duis enim velit mollit.</p>
  <a class="btn shop">Shop Now <svg viewBox="0 0 12 12"><path d="M1 6h9M6 2l4 4-4 4" stroke="currentColor" stroke-width="1.6" fill="none"/></svg></a>
</div>
<div class="promo" style="left:617px">
  <h3 class="display">JOIN OUR CLUB</h3>
  <p>Amet minim mollit non deserunt ullamco est sit aliqua dolor do amet sint. Velit officia consequat duis enim velit mollit.</p>
  <a class="btn shop">Shop Now <svg viewBox="0 0 12 12"><path d="M1 6h9M6 2l4 4-4 4" stroke="currentColor" stroke-width="1.6" fill="none"/></svg></a>
</div>
<div class="player" style="left:20px;top:2030px;width:200px;height:300px" role="img" aria-label="Cut-out photo of a player in a red, white and blue uniform"></div>
<div class="player" style="left:955px;top:2025px;width:245px;height:300px;background:radial-gradient(ellipse at 50% 50%,#e9a867 0%,#4a5a9a 42%,rgba(255,255,255,0) 72%)" role="img" aria-label="Cut-out photo of a player in an orange and blue uniform"></div>

</body>
</html>
```